New Company Business Card Design

I have a new company logo and I want a new business card design. I dont know if the logo file i attached is in the correct format or quality. We are a New York City Specialty construction Firm specializing in high risk out of the box projects. I want a simple and classy business card that people will his card is as crisp as the work his company does.

Target Market(s)

Clients in the heavy construction industry in New York City

Industry/Entity Type

Construction Company

Contact Information for Business Card

Simple Classy - DIFFERENT

Font styles to use
Other font styles liked:
• Mach the logo font in some way

Colors

Designer to choose colors to be used in the design.

Requirements
Must have
• Uniqueness
Nice to have
• Nothing particular - Just different and classy - Timeless
Should not have
• Goofy Shit or Gimmicky shit

```html
<!DOCTYPE html>
<html lang="en">
<head>
<meta charset="utf-8">
<title>Korven Associates – Business Card</title>
<link rel="stylesheet" href="https://fonts.googleapis.com/css2?family=Oswald:wght@500;700&family=Lato:wght@400&display=swap">
<style>
  :root {
    --page-bg: #2b2b2b;
    --card-bg: #fbfbfb;
    --brand-blue: #1b4a93;
    --logo-blue: #1670b5;
    --ink: #2a2a2a;
    --band-dark: #373737;
  }
  * { box-sizing: border-box; margin: 0; padding: 0; }
  html, body { width: 1200px; height: 1200px; overflow: hidden; }
  body { background: var(--page-bg); position: relative; font-family: "Lato", sans-serif; color: var(--ink); }

  .card { position: absolute; left: 167px; width: 815px; height: 466px; background: var(--card-bg); overflow: hidden; }
  .card--front { top: 74px; }
  .card--back { top: 657px; }

  /* front */
  .brand-name { position: absolute; font-family: "Oswald", sans-serif; font-weight: 700; color: var(--logo-blue); text-transform: uppercase; }
  .card--front .brand-name { left: 466px; top: 92px; width: 272px; text-align: center; line-height: 1; }
  .card--front .brand-name .brand-main { display: block; font-size: 74px; letter-spacing: 4px; }
  .card--front .brand-name .brand-sub { display: block; font-size: 19px; letter-spacing: 6px; margin-top: 8px; }

  .person-name { position: absolute; left: 46px; top: 264px; font-family: "Oswald", sans-serif; font-weight: 500; font-size: 34px; color: var(--brand-blue); letter-spacing: 0.5px; line-height: 1; }
  .person-role { position: absolute; left: 46px; top: 305px; font-size: 17px; line-height: 1; }
  .divider { position: absolute; left: 46px; top: 333px; width: 692px; height: 3px; background: var(--brand-blue); }

  .contact-list { position: absolute; left: 46px; top: 339px; list-style: none; }
  .contact-list li { display: flex; align-items: center; height: 25.5px; font-size: 18px; }
  .contact-list svg { width: 18px; height: 18px; margin-right: 18px; flex: none; }

  .address { position: absolute; left: 466px; top: 347px; font-size: 18px; line-height: 22px; }

  .band { position: absolute; top: 438px; height: 28px; }
  .band--blue { left: 0; width: 466px; background: var(--brand-blue); }
  .band--dark { left: 466px; right: 0; background: var(--band-dark); }

  /* back */
  .card--back .brand-name { left: 0; right: 0; top: 120px; text-align: center; line-height: 1; }
  .card--back .brand-name .brand-main { display: block; font-size: 190px; letter-spacing: 14px; }
  .card--back .brand-name .brand-sub { display: block; font-size: 48px; letter-spacing: 16px; margin-top: 24px; }
</style>
</head>
<body>
  <section class="card card--front">
    <div class="brand-name"><span class="brand-main">Korven</span><span class="brand-sub">Associates, Inc.</span></div>

    <h1 class="person-name">DANIEL ROURKE</h1>
    <p class="person-role">manager</p>
    <div class="divider"></div>

    <ul class="contact-list">
      <li>
        <svg viewBox="0 0 24 24" fill="none" stroke="#1b4a93" stroke-width="2.2" stroke-linecap="round" stroke-linejoin="round"><path d="M5 3h4l2 5-2.5 1.5a11 11 0 0 0 6 6L16 13l5 2v4a2 2 0 0 1-2 2A17 17 0 0 1 3 5a2 2 0 0 1 2-2z"/><path d="M15 3a6 6 0 0 1 6 6M15 7a2 2 0 0 1 2 2"/></svg>
        +1 212-555-0148
      </li>
      <li>
        <svg viewBox="0 0 24 24" fill="none" stroke="#1b4a93" stroke-width="1.8" stroke-linejoin="round"><rect x="2" y="5" width="20" height="14"/><path d="M2 5l10 8 10-8M2 19l8-7M22 19l-8-7"/></svg>
        d.rourke@korvenbuild.com
      </li>
      <li>
        <svg viewBox="0 0 24 24" fill="none" stroke="#1b4a93" stroke-width="1.8"><circle cx="12" cy="12" r="10"/><ellipse cx="12" cy="12" rx="4.5" ry="10"/><path d="M2 12h20M4 7h16M4 17h16"/></svg>
        www.korvenbuild.com
      </li>
    </ul>

    <p class="address">48 Harbor Point Avenue 12<br>NEW YORK - NY 10004</p>

    <div class="band band--blue"></div>
    <div class="band band--dark"></div>
  </section>

  <section class="card card--back">
    <div class="brand-name"><span class="brand-main">Korven</span><span class="brand-sub">Associates, Inc.</span></div>
  </section>
</body>
</html>
```